" A empresa tem como principal atrativo a grande variedade de joias infantis. Nosso maior diferencial são as peças de alta joalheria para crianças e a confecção de joias exclusivas e personalizadas para o publico de todas as idades. Temos um atelier para atendimento com hora marcada e o e-commerce é nossa principal vitrine. É possível conhecer algumas peças e parte da identidade da marca no nosso site www.brilhomirim.com.br e no instagram @brilhomirim "

```html
<!DOCTYPE html>
<html lang="pt-BR">
<head>
<meta charset="utf-8">
<title>Brilho Mirim – Caderno</title>
<link rel="stylesheet" href="https://fonts.googleapis.com/css2?family=Cinzel:wght@400&family=Montserrat:wght@400;500&display=swap">
<style>
  :root {
    --stage: #f1eee9;
    --cover-blue: #bcdcf3;
    --paper: #ffffff;
    --ink: #2b2b2b;
    --band-grey: #8c8c8c;
    --rule-grey: #a9a9a9;
    --brand-blue: #7fb3d8;
    --deco-blue: #e6f2fb;
    --deco-grey: #f0f0f0;
  }
  * { box-sizing: border-box; margin: 0; padding: 0; }
  html, body { width: 1200px; height: 1200px; overflow: hidden; }
  body {
    position: relative;
    background: var(--stage);
    font-family: "Montserrat", sans-serif;
    color: var(--ink);
  }
  .piece-label {
    position: absolute;
    font-size: 22px;
    font-weight: 400;
  }
  .label-front { left: 256px; top: 14px; }
  .label-back { left: 836px; top: 14px; }
  .label-inner { left: 318px; top: 958px; }

  .sheet {
    position: absolute;
    box-shadow: 0 2px 6px rgba(0,0,0,.18);
    overflow: hidden;
  }
  .front-cover {
    left: 84px; top: 60px; width: 545px; height: 560px;
    background: var(--cover-blue);
  }
  .brand-name {
    font-family: "Cinzel", serif;
    font-weight: 400;
    letter-spacing: 3px;
  }
  .front-cover .brand-name {
    position: absolute;
    left: 0; right: 0; top: 250px;
    text-align: center;
    font-size: 46px;
    color: #ffffff;
  }
  .front-url {
    position: absolute;
    left: 60px; bottom: 22px;
    font-size: 13px;
    letter-spacing: 7px;
    color: #6f8ea5;
  }

  .back-cover {
    left: 643px; top: 60px; width: 540px; height: 560px;
    background: var(--paper);
  }
  .deco-area {
    position: absolute;
    border-radius: 40% 40% 30% 30%;
    background: linear-gradient(180deg, var(--deco-grey) 0%, var(--deco-blue) 45%, #f4f9fd 100%);
  }
  .back-cover .deco-area { left: 50px; top: 60px; width: 440px; height: 410px; }
  .contact-band {
    position: absolute;
    left: 0; right: 0; bottom: 0; height: 46px;
    background: var(--band-grey);
    color: #ffffff;
    font-size: 7px;
    line-height: 10px;
    text-align: center;
    padding-top: 8px;
  }

  .inner-page {
    left: 413px; top: 628px; width: 542px; height: 560px;
    background: var(--paper);
  }
  .inner-page .brand-name {
    position: absolute;
    left: 24px; top: 38px;
    font-size: 15px;
    letter-spacing: 1px;
    color: var(--brand-blue);
  }
  .date-box {
    position: absolute;
    right: 34px; top: 30px;
    width: 160px; height: 28px;
    border: 1.5px solid var(--ink);
    display: flex;
    justify-content: space-evenly;
    align-items: center;
    font-size: 18px;
    padding-left: 40px;
  }
  .inner-page .deco-area { left: 60px; top: 140px; width: 430px; height: 390px; opacity: .8; }
  .ruled-lines { position: absolute; left: 24px; right: 24px; top: 98px; bottom: 20px; }
</style>
</head>
<body>
  <span class="piece-label label-front">Frente</span>
  <span class="piece-label label-back">Contra Capa</span>
  <span class="piece-label label-inner">Miolo</span>

  <section class="sheet front-cover">
    <div class="brand-name">Brilho Mirim</div>
    <div class="front-url">www.brilhomirim.com.br</div>
  </section>

  <section class="sheet back-cover">
    <div class="deco-area" role="img" aria-label="Ilustração suave de laço de fita com pedra lapidada, em linhas azul-claras"></div>
    <div class="contact-band">
      <div>Rua das Joias 120 São Paulo</div>
      <div>Tel (11) 4000-1200</div>
      <div>contato@brilhomirim.com.br @brilhomirim</div>
    </div>
  </section>

  <section class="sheet inner-page">
    <div class="brand-name">Brilho Mirim</div>
    <div class="date-box"><span>/</span><span>/</span></div>
    <div class="deco-area" role="img" aria-label="Ilustração suave de laço de fita com pedra lapidada, em linhas azul-claras"></div>
    <svg class="ruled-lines" width="494" height="442" viewBox="0 0 494 442" aria-hidden="true">
      <g stroke="#a9a9a9" stroke-width="1.5">
        <line x1="0" x2="494" y1="2" y2="2"/><line x1="0" x2="494" y1="22" y2="22"/>
        <line x1="0" x2="494" y1="42" y2="42"/><line x1="0" x2="494" y1="62" y2="62"/>
        <line x1="0" x2="494" y1="82" y2="82"/><line x1="0" x2="494" y1="102" y2="102"/>
        <line x1="0" x2="494" y1="122" y2="122"/><line x1="0" x2="494" y1="142" y2="142"/>
        <line x1="0" x2="494" y1="162" y2="162"/><line x1="0" x2="494" y1="182" y2="182"/>
        <line x1="0" x2="494" y1="202" y2="202"/><line x1="0" x2="494" y1="222" y2="222"/>
        <line x1="0" x2="494" y1="242" y2="242"/><line x1="0" x2="494" y1="262" y2="262"/>
        <line x1="0" x2="494" y1="282" y2="282"/><line x1="0" x2="494" y1="302" y2="302"/>
        <line x1="0" x2="494" y1="322" y2="322"/><line x1="0" x2="494" y1="342" y2="342"/>
        <line x1="0" x2="494" y1="362" y2="362"/><line x1="0" x2="494" y1="382" y2="382"/>
        <line x1="0" x2="494" y1="402" y2="402"/><line x1="0" x2="494" y1="422" y2="422"/>
      </g>
    </svg>
  </section>
</body>
</html>
```